Fernvale Pantry web design

Go to fernvalepantry.com.au an using the current layout create a design that will attract customers to this wholefood website.

You may suggest / make slight changes to the layout to create effective graphic design principles.

The LOGO design is TM already. So no changes there. Second logo attached is authorised for use and is a area branding LOGO.

Colours need to reflect health and wellbeing.

Don't want Medical style or New age.
Updates

Logo now loaded

Thank you for your submissions so far. I have sent them out to a trusty panel of friends to hear what they have to say. Some of you have done very well.

Project Deadline Extended
Reason: There are a few submissions outstanding. I will eliminate a few designs today and give feed back. Thankyou

Thank you for your submissions so far I will not be asking for more design submissions from other designers. The ones I have are under consideration and there are a few minor changes to each that may just bring out the one that is IT! The two designs I have narrowed it down to are very different in approach so please bear with me a couple more days. Thank you.

Target Market(s)

Whole food health concious people target market locally Home Delivery would be young Mums with restricted movement because of young children. Older people that are restricted transport users.

Busy commuters that leave our area for work and just want to relax on the weekend with their family and local bush walking or garden activities.

Industry/Entity Type

Graphic Design

Requirements
Should not have
• Medical or sterile hospital feel. New age or too alternative living feel.

```html
<!DOCTYPE html>
<html lang="en">
<head>
<meta charset="utf-8">
<title>Fernvale Pantry</title>
<link href="https://fonts.googleapis.com/css2?family=PT+Sans:ital,wght@0,400;0,700;1,400&family=Oswald:wght@400;500&family=Marcellus+SC&display=swap" rel="stylesheet">
<style>
:root{
  --purple:#6e1468;
  --orange:#f0561a;
  --topbar:#e6e6e6;
  --header:#f1f1f1;
  --text:#444;
  --line:#d9d9d9;
  --footer:#2e333f;
  --footer-text:#c9ccd3;
  --green:#2fa24a;
  --olive:#d8d4a8;
  --sale-blue:#3f62a4;
  --navy:#1b3a7a;
  --red:#d6361e;
}
*{box-sizing:border-box;margin:0;padding:0}
html,body{width:1200px;height:2632px;overflow:hidden}
body{font-family:"PT Sans",Arial,sans-serif;color:var(--text);background:#fff;position:relative;font-size:13px}
.abs{position:absolute}

/* top bar */
.topbar{left:0;top:0;width:1200px;height:49px;background:var(--topbar);border-top:5px solid var(--purple)}
.select{top:9px;height:26px;background:#d6d6d6;border:1px solid #c4c4c4;font-size:12px;color:#666;padding:5px 8px}
.select .caret{position:absolute;right:-1px;top:-1px;width:30px;height:26px;background:var(--purple)}
.select .caret svg{position:absolute;left:9px;top:9px}
.toplinks{right:81px;top:0;height:44px;display:flex;font-size:12.5px;color:#777}
.toplinks a{padding:0 10px;line-height:44px;border-left:1px solid #d2d2d2}
.toplinks a:first-child{border-left:none}
.toplinks a.active{background:#d3d3d3;border-bottom:3px solid var(--purple);color:var(--purple)}

/* header */
.header{left:0;top:49px;width:1200px;height:146px;background:var(--header)}
.brand{left:104px;top:104px;display:flex;align-items:center;gap:10px}
.brand .dot{width:26px;height:26px;border-radius:50%;background:var(--green)}
.brand span{font-size:25px;font-weight:700;color:var(--purple)}
.info{top:72px;display:flex;gap:10px}
.info svg{flex:none;margin-top:2px}
.info b{display:block;font-size:14px;color:#555;font-weight:700}
.info small{font-size:11.5px;color:#777}
.search{left:403px;top:140px;width:490px;height:35px;background:#fff;border:1px solid #e2e2e2;font-size:11.5px;color:#aaa;padding:9px 14px}
.search .go{position:absolute;right:-1px;top:-1px;width:34px;height:35px;background:var(--purple)}
.search .go svg{position:absolute;left:9px;top:9px}
.cart{left:953px;top:130px;display:flex;gap:10px}
.cart b{display:block;font-size:14px;color:#555}
.cart small{font-size:12px;color:#777}

/* nav */
.nav{left:89px;top:195px;width:1030px;height:38px;display:flex;font-size:15.5px;color:#555;letter-spacing:.3px}
.nav a{padding:0 11px;line-height:38px;text-transform:uppercase}
.nav a.home{background:var(--purple);color:#fff}
.nav .special{margin-left:auto;display:flex;background:var(--orange)}
.nav .special a{color:#fff;padding:0 13px}
.nav .special a+a{border-left:1px solid #fff}
.navline{left:0;top:233px;width:1200px;height:1px;background:var(--line)}

/* slider */
.slider{left:89px;top:245px;width:1030px;height:412px;border:1px solid #ddd;padding:7px;background:#fff;box-shadow:0 1px 3px rgba(0,0,0,.12)}
.slider .photo{width:100%;height:100%;background:radial-gradient(circle at 30% 30%,#f6d37a 0,#e8913a 35%,#c2401e 70%,#8e2a14 100%)}
.caption-title{left:226px;top:370px;background:rgba(30,30,30,.82);color:#fff;font-family:"Oswald",sans-serif;font-size:36px;padding:2px 22px 4px}
.caption-sub{left:226px;top:438px;background:#fff;color:#333;font-family:"Oswald",sans-serif;font-size:18px;padding:4px 12px}
.dots{left:496px;top:620px;display:flex;gap:14px}
.dots i{display:block;width:52px;height:4px;background:#fff}
.dots i:first-child{background:var(--purple)}

/* section titles */
.section-title{left:98px;width:748px;font-family:"Marcellus SC",serif;font-size:22px;color:#666;letter-spacing:1px;padding-bottom:8px;border-bottom:2px solid #c9c9d8}

/* deals */
.deal{width:170px;text-align:center}
.deal .pic{height:135px;margin:0 12px}
.deal h3{font-size:12.5px;color:var(--purple);text-transform:uppercase;margin-top:14px;letter-spacing:.3px}
.deal p{font-size:11.5px;color:#555;line-height:1.3;margin-top:9px;height:46px}
.deal .row{display:flex;justify-content:center;align-items:center;gap:8px;font-size:11.5px}
.deal .row b{font-weight:400}
.btn-buy{background:var(--purple);color:#fff;font-size:10.5px;font-weight:700;padding:2px 6px}
.bottle{background:linear-gradient(#fff,#fff 15%,#5b9a3a 40%,#e8e6d5 85%,#fff)}
.jar{background:linear-gradient(#fff,#f3c23d 25%,#e6a818 60%,#fff)}
.tea{background:linear-gradient(#fff,#a5cf5a 35%,#e9efe6 70%,#fff)}
.chips{background:linear-gradient(135deg,#fff,#3a63c4 30%,#e34328 55%,#f2c42a 75%,#fff)}

/* recipes */
.recipe{width:167px;height:243px;border:1px solid var(--olive);background:#fff;padding:5px}
.recipe .pic{height:116px}
.recipe p{font-size:11.5px;color:#444;line-height:1.5;margin:14px 2px 0}
.recipe .price{font-size:12.5px;color:var(--purple);margin:8px 2px 0}
.recipe .foot{display:flex;justify-content:space-between;align-items:center;margin:8px 2px 0}
.recipe .buy{border:1px solid #d7d38d;border-radius:10px;background:#fbf9e3;font-size:10.5px;color:var(--orange);padding:1px 14px}
.recipe .likes{font-size:10.5px;color:#888;display:flex;align-items:center;gap:6px}
.burger{background:linear-gradient(#f5f5f5,#e2a457 40%,#c7461e 60%,#e8b969 80%,#f5f5f5)}
.salad{background:radial-gradient(circle at 40% 50%,#f3e4a0,#7aa63c 40%,#3c6a2a 80%)}
.toast{background:radial-gradient(circle at 50% 55%,#e88f63,#f0d3a8 45%,#fbfbfb 80%)}
.sandwich{background:linear-gradient(160deg,#f5efe0,#e2bd5c 30%,#d8472d 55%,#88b44a 75%,#f2f2f2)}

/* sidebar */
.sale{left:886px;top:672px;width:231px;height:100px;background:var(--sale-blue);border:4px solid #ced6e8}
.sale .inner{position:absolute;inset:6px;border:2px solid #fff;color:#fff;font-family:"Oswald",sans-serif;font-weight:500;line-height:1;padding:6px 10px;white-space:nowrap}
.sale .small{font-size:22px;display:block}
.sale .big{display:flex;align-items:baseline;gap:6px}
.sale .big span{font-size:32px}
.sale .big b{font-size:44px;font-weight:500;margin-top:-14px}
.cat-box{left:886px;width:232px;border:1px solid #cfcfcf;background:#fff}
.cat-head{height:38px;background:var(--purple);border-bottom:3px solid #e4c46a;display:flex;align-items:center;color:#fff;font-family:"Marcellus SC",serif;font-size:17px}
.cat-head .icon{width:38px;height:35px;border-right:1px solid rgba(255,255,255,.4);display:flex;align-items:center;justify-content:center;margin-right:12px}
.cat-box ul{list-style:none;padding-top:3px}
.cat-box li{height:26.6px;display:flex;align-items:center;justify-content:space-between;margin-left:4px;padding:0 14px 0 20px;border-bottom:1px solid #e3e3e3;font-size:11.5px;color:#777;text-transform:uppercase;letter-spacing:1px}
.cat-box li::after{content:"+";color:#777;font-size:13px}
.cat-box li.on{border-left:4px solid var(--purple);margin-left:0;color:var(--purple)}
.cat-box li.more{border-bottom:none}
.cat-box li.more::after{content:""}

/* promo row */
.newsletter{left:100px;top:1883px;width:361px;height:138px;background:linear-gradient(90deg,#9a9a8e 0,#6f6f6f 40%,#5c5c5c 100%)}
.newsletter .bag{position:absolute;left:0;top:0;width:180px;height:138px;background:linear-gradient(135deg,#c8c3b2,#8c8a7d 50%,#6a7a4a)}
.newsletter h4{position:absolute;left:194px;top:30px;color:#eee;font-weight:400;font-size:17px;letter-spacing:.5px}
.newsletter h5{position:absolute;left:194px;top:51px;color:#ddd;font-weight:400;font-size:11.5px;letter-spacing:.5px}
.newsletter .field{position:absolute;left:194px;top:79px;width:126px;height:19px;background:#444;font-size:9.5px;color:#ddd;padding:3px 5px}
.newsletter .go{position:absolute;left:320px;top:79px;width:26px;height:19px;background:#e98a1e;color:#fff;font-size:11px;font-weight:700;text-align:center;line-height:19px}
.appbanner{left:479px;top:1883px;width:267px;height:138px;background:linear-gradient(#f6f6f6,#dcdcdc)}
.appbanner .phone{position:absolute;left:24px;top:6px;width:58px;height:124px;border-radius:8px;background:#1f1f1f}
.appbanner .phone i{position:absolute;left:5px;top:14px;right:5px;bottom:16px;background:linear-gradient(#e64b2a,#f1b335)}
.appbanner .txt{position:absolute;left:99px;top:8px;font-family:"Oswald",sans-serif;line-height:1;white-space:nowrap}
.appbanner .txt .o{color:var(--red);font-size:24px}
.appbanner .txt .g{color:var(--navy);font-size:35px}
.appbanner .txt .h{color:var(--navy);font-size:27px}
.appbanner .dl{position:absolute;left:164px;top:112px;width:70px;height:14px;background:var(--purple);color:#fff;font-size:8px;text-align:center;line-height:14px}
.payment{left:763px;top:1883px;width:351px;height:138px;background:linear-gradient(90deg,#fbf8e6,#f1eed6)}
.payment h4{position:absolute;left:0;right:0;top:14px;text-align:center;font-family:"Oswald",sans-serif;font-weight:400;font-size:20px;color:#333;letter-spacing:1px}
.payment .cod{position:absolute;left:22px;top:63px;font-family:"Oswald",sans-serif;font-size:25px;line-height:1.1;color:#2a6bb8}
.payment .cod span{color:#e0341e}
.payment .cards{position:absolute;left:158px;top:64px;display:grid;grid-template-columns:repeat(5,34px);gap:6px}
.payment .cards i{display:block;height:22px;background:#fff;border:1px solid #cfcfcf}

/* welcome */
.welcome{left:89px;top:2050px;width:1030px;display:flex;align-items:center;gap:14px;font-size:27px;color:#9a9a9a;letter-spacing:1px}
.welcome::before,.welcome::after{content:"";flex:1;height:2px;background:var(--purple)}
.ribbon{left:225px;top:2112px;width:736px;height:64px}
.ribbon .band{position:absolute;left:60px;right:60px;top:4px;height:52px;background:linear-gradient(#f4f4f4,#dedede);box-shadow:0 2px 3px rgba(0,0,0,.15);text-align:center;line-height:52px;font-size:19px;color:#444;letter-spacing:1.5px}
.intro{left:170px;top:2204px;width:860px;text-align:center;font-size:17px;line-height:1.6;color:#444}

/* footer */
.footer{left:0;top:2339px;width:1200px;height:266px;background:var(--footer);color:var(--footer-text)}
.fcol{position:absolute;top:38px}
.fcol h6{font-size:13px;font-weight:400;color:#fff;text-transform:uppercase;letter-spacing:.5px;padding-bottom:8px;position:relative}
.fcol h6::after{content:"";position:absolute;left:0;bottom:0;width:36px;height:2px;background:var(--orange)}
.fcol ul{list-style:none;margin-top:14px}
.fcol li{font-size:11.5px;line-height:29.5px}
.fcol li::before{content:"• "}
.fcol li.on{color:#7ed07d}
.quote{font-size:11.5px;line-height:24px;font-style:italic;margin-top:14px;width:230px}
.quote .by{text-align:right;margin-top:2px}
.contact p{font-size:11.5px;line-height:24px;font-style:italic;margin-top:4px}
.social{display:flex;gap:6px;margin-top:8px}
.social i{display:block;width:23px;height:23px;background:#111}
.bottombar{left:0;top:2605px;width:1200px;height:27px;background:var(--purple);color:#e6d6e6;font-size:10.5px;font-style:italic;text-align:center;line-height:27px;letter-spacing:.5px}
</style>
</head>
<body>

<!-- top utility bar -->
<div class="abs topbar"></div>
<div class="abs select" style="left:105px;width:167px">Choose Your Place<span class="caret"><svg width="12" height="8"><path d="M1 1l5 5 5-5" stroke="#fff" stroke-width="2" fill="none"/></svg></span></div>
<div class="abs select" style="left:284px;width:181px">Check our delivery slots<span class="caret"><svg width="12" height="8"><path d="M1 1l5 5 5-5" stroke="#fff" stroke-width="2" fill="none"/></svg></span></div>
<nav class="abs toplinks"><a>My Account</a><a class="active">Wishlist</a><a>My Cart</a><a>Checkout</a><a>Login / Register</a></nav>

<!-- header -->
<div class="abs header"></div>
<div class="abs brand"><i class="dot"></i><span>Fernvale Pantry</span></div>
<div class="abs info" style="left:336px"><svg width="26" height="22"><rect x="1" y="3" width="15" height="12" fill="#666"/><path d="M16 7h5l4 4v4h-9z" fill="#666"/><circle cx="6" cy="17" r="3" fill="#666"/><circle cx="20" cy="17" r="3" fill="#666"/></svg><div><b>FREE DELIVERY FOR ORDERS</b><small>RS. 1000.00 AND ABOVE</small></div></div>
<div class="abs info" style="left:632px"><svg width="24" height="24"><path d="M8 2h8l-2 5h-4z" fill="#666"/><path d="M9 8h6c5 4 7 14-3 14S4 12 9 8z" fill="#666"/></svg><div><b>100% MONEY BACK</b><small>30 Days Money Back Guarantee</small></div></div>
<div class="abs info" style="left:913px"><svg width="26" height="22"><path d="M2 8c6-6 16-6 22 0l-3 4-4-2v-3c-3-1-5-1-8 0v3l-4 2z" fill="#666"/><rect x="6" y="13" width="14" height="8" fill="#666"/></svg><div><b>PHONE : 0400-555-218</b><small>Order Online Now !</small></div></div>
<div class="abs search">Search for more than 10,000 products..<span class="go"><svg width="16" height="16"><circle cx="6.5" cy="6.5" r="5" stroke="#fff" stroke-width="2" fill="none"/><path d="M10 10l5 5" stroke="#fff" stroke-width="2"/></svg></span></div>
<div class="abs cart"><svg width="30" height="28"><path d="M3 10h24l-3 16H6z" fill="#2d5f9e"/><path d="M9 10c0-8 12-8 12 0" stroke="#2d5f9e" stroke-width="2.5" fill="none"/></svg><div><b>SHOPPING CART</b><small>0 item (s) - $0.00</small></div></div>

<!-- main nav -->
<nav class="abs nav">
  <a class="home">Home</a><a>By Categories</a><a>Purchase by Weight</a><a>By Brands</a><a>Recipes</a><a>Blog</a><a>Contact</a>
  <div class="special"><a>Today's Special</a><a>Combo Offers</a></div>
</nav>
<div class="abs navline"></div>

<!-- hero slider -->
<div class="abs slider"><div class="photo" role="img" aria-label="Close-up of a pizza with peppers, onions and olives"></div></div>
<div class="abs caption-title">Delicious Pizza</div>
<div class="abs caption-sub">SLIDER DESCRIPTION GOES HERE!</div>
<div class="abs dots"><i></i><i></i><i></i><i></i></div>

<!-- latest deals -->
<h2 class="abs section-title" style="top:694px">Latest Deals</h2>

<div class="abs deal" style="left:106px;top:754px"><div class="pic bottle" role="img" aria-label="Supplement bottle"></div><h3>Inner Balance Plus 30C</h3><p>Verdant Pure™ 100% Pure Garcinia Cambogia 1000mg 60% HCA (90 Capsules)</p><div class="row"><b>Price &nbsp;: $35.50</b><span class="btn-buy">BUY NOW</span></div></div>
<div class="abs deal" style="left:292px;top:754px"><div class="pic jar" role="img" aria-label="Jars of peanut butter"></div><h3>Fresh Peanut Butter</h3><p>This nut butter has absolutely no additives. Just only penuts</p><div class="row"><b>Price &nbsp;: $20.50</b><span class="btn-buy">BUY NOW</span></div></div>
<div class="abs deal" style="left:478px;top:754px"><div class="pic tea" role="img" aria-label="Green tea box with fresh mint"></div><h3>Organic Green Teas</h3><p>12 x 25's (sachets) of Organic Green Tea with Peppermint &amp; Lemon Flovour</p><div class="row"><b>Price &nbsp;: $15.50</b><span class="btn-buy">BUY NOW</span></div></div>
<div class="abs deal" style="left:664px;top:754px"><div class="pic chips" role="img" aria-label="Bags of healthy snack chips"></div><h3>Healthy Snacks</h3><p>Healthy Chips, Biscuits, Cakes</p><div class="row"><b>Price &nbsp;: $15.50</b><span class="btn-buy">BUY NOW</span></div></div>

<div class="abs deal" style="left:106px;top:1004px"><div class="pic bottle" role="img" aria-label="Supplement bottle"></div><h3>Inner Balance Plus 30C</h3><p>Verdant Pure™ 100% Pure Garcinia Cambogia 1000mg 60% HCA (90 Capsules)</p><div class="row"><b>Price &nbsp;: $35.50</b><span class="btn-buy">BUY NOW</span></div></div>
<div class="abs deal" style="left:292px;top:1004px"><div class="pic jar" role="img" aria-label="Jars of peanut butter"></div><h3>Fresh Peanut Butter</h3><p>This nut butter has absolutely no additives. Just only penuts</p><div class="row"><b>Price &nbsp;: $20.50</b><span class="btn-buy">BUY NOW</span></div></div>
<div class="abs deal" style="left:478px;top:1004px"><div class="pic tea" role="img" aria-label="Green tea box with fresh mint"></div><h3>Organic Green Teas</h3><p>12 x 25's (sachets) of Organic Green Tea with Peppermint &amp; Lemon Flovour</p><div class="row"><b>Price &nbsp;: $15.50</b><span class="btn-buy">BUY NOW</span></div></div>
<div class="abs deal" style="left:664px;top:1004px"><div class="pic chips" role="img" aria-label="Bags of healthy snack chips"></div><h3>Healthy Snacks</h3><p>Healthy Chips, Biscuits, Cakes</p><div class="row"><b>Price &nbsp;: $15.50</b><span class="btn-buy">BUY NOW</span></div></div>

<!-- todays recipes -->
<h2 class="abs section-title" style="top:1273px">Todays Recipes</h2>

<div class="abs recipe" style="left:100px;top:1337px"><div class="pic burger" role="img" aria-label="Burger on a white plate"></div><p>Lorem ipsum dolor sit amet, consectetuer adipiscing elit</p><div class="price">Price: <b>$12.00</b></div><div class="foot"><span class="buy">BUY</span><span class="likes"><svg width="12" height="11"><path d="M6 10L1 5a3 3 0 015-3 3 3 0 015 3z" fill="#aaa"/></svg>120</span></div></div>
<div class="abs recipe" style="left:292px;top:1337px"><div class="pic salad" role="img" aria-label="Green salad with egg and ham"></div><p>Lorem ipsum dolor sit amet, consectetuer adipiscing elit</p><div class="price">Price: <b>$12.00</b></div><div class="foot"><span class="buy">BUY</span><span class="likes"><svg width="12" height="11"><path d="M6 10L1 5a3 3 0 015-3 3 3 0 015 3z" fill="#aaa"/></svg>120</span></div></div>
<div class="abs recipe" style="left:484px;top:1337px"><div class="pic toast" role="img" aria-label="Open sandwich with tomato"></div><p>Lorem ipsum dolor sit amet, consectetuer adipiscing elit</p><div class="price">Price: <b>$12.00</b></div><div class="foot"><span class="buy">BUY</span><span class="likes"><svg width="12" height="11"><path d="M6 10L1 5a3 3 0 015-3 3 3 0 015 3z" fill="#aaa"/></svg>120</span></div></div>
<div class="abs recipe" style="left:676px;top:1337px"><div class="pic sandwich" role="img" aria-label="Layered sandwich with a fork"></div><p>Lorem ipsum dolor sit amet, consectetuer adipiscing elit</p><div class="price">Price: <b>$12.00</b></div><div class="foot"><span class="buy">BUY</span><span class="likes"><svg width="12" height="11"><path d="M6 10L1 5a3 3 0 015-3 3 3 0 015 3z" fill="#aaa"/></svg>120</span></div></div>

<div class="abs recipe" style="left:100px;top:1603px"><div class="pic burger" role="img" aria-label="Burger on a white plate"></div><p>Lorem ipsum dolor sit amet, consectetuer adipiscing elit</p><div class="price">Price: <b>$12.00</b></div><div class="foot"><span class="buy">BUY</span><span class="likes"><svg width="12" height="11"><path d="M6 10L1 5a3 3 0 015-3 3 3 0 015 3z" fill="#aaa"/></svg>120</span></div></div>
<div class="abs recipe" style="left:292px;top:1603px"><div class="pic salad" role="img" aria-label="Green salad with egg and ham"></div><p>Lorem ipsum dolor sit amet, consectetuer adipiscing elit</p><div class="price">Price: <b>$12.00</b></div><div class="foot"><span class="buy">BUY</span><span class="likes"><svg width="12" height="11"><path d="M6 10L1 5a3 3 0 015-3 3 3 0 015 3z" fill="#aaa"/></svg>120</span></div></div>
<div class="abs recipe" style="left:484px;top:1603px"><div class="pic toast" role="img" aria-label="Open sandwich with tomato"></div><p>Lorem ipsum dolor sit amet, consectetuer adipiscing elit</p><div class="price">Price: <b>$12.00</b></div><div class="foot"><span class="buy">BUY</span><span class="likes"><svg width="12" height="11"><path d="M6 10L1 5a3 3 0 015-3 3 3 0 015 3z" fill="#aaa"/></svg>120</span></div></div>
<div class="abs recipe" style="left:676px;top:1603px"><div class="pic sandwich" role="img" aria-label="Layered sandwich with a fork"></div><p>Lorem ipsum dolor sit amet, consectetuer adipiscing elit</p><div class="price">Price: <b>$12.00</b></div><div class="foot"><span class="buy">BUY</span><span class="likes"><svg width="12" height="11"><path d="M6 10L1 5a3 3 0 015-3 3 3 0 015 3z" fill="#aaa"/></svg>120</span></div></div>

<!-- sidebar -->
<div class="abs sale"><div class="inner"><span class="small">BIGGEST</span><div class="big"><span>SALE</span><b>EVER</b></div></div></div>

<aside class="abs cat-box" style="top:788px">
  <div class="cat-head"><span class="icon"><svg width="16" height="12"><g fill="#fff"><rect width="3" height="2"/><rect x="5" width="11" height="2"/><rect y="5" width="3" height="2"/><rect x="5" y="5" width="11" height="2"/><rect y="10" width="3" height="2"/><rect x="5" y="10" width="11" height="2"/></g></svg></span>Product Categories</div>
  <ul>
    <li>Alternative Goods</li><li>Dairy Free</li><li>Gluten Free</li><li class="on">Grocery</li><li>Health Suppliments</li><li>Natural Grocer</li><li>Organic</li><li>Recipes</li><li>Seasonal</li><li>Specials</li><li>Sugar Replacements</li><li>Vegan</li><li>Vegetarian</li><li class="more">More &gt;&gt;</li>
  </ul>
</aside>

<aside class="abs cat-box" style="top:1219px;height:601px">
  <div class="cat-head"><span class="icon"><svg width="16" height="12"><g fill="#fff"><rect width="3" height="2"/><rect x="5" width="11" height="2"/><rect y="5" width="3" height="2"/><rect x="5" y="5" width="11" height="2"/><rect y="10" width="3" height="2"/><rect x="5" y="10" width="11" height="2"/></g></svg></span>Product Categories</div>
  <ul>
    <li>Baking</li><li>Beans &amp; Pea</li><li>Candy &amp; Sweet Treats</li><li class="on">Cereals Granolas</li><li>Coffee &amp; Tea</li><li>Dried Fruit</li><li>Flour</li><li>Free Range Meat</li><li>Processed Meat</li><li>Grain</li><li>Honey Sugar</li><li>Natural Replacement</li><li>Museli</li><li>Nuts</li><li>Pasta</li><li>Pasture Grazed Lamb</li><li>Seeds</li><li>Snacks</li><li>Specials</li><li class="more">More &gt;&gt;</li>
  </ul>
</aside>

<!-- promo banners -->
<div class="abs newsletter">
  <div class="bag" role="img" aria-label="Grocery bag with bread and vegetables"></div>
  <h4>SUBSCRIBE</h4><h5>OUR NEWSLETTER</h5>
  <div class="field">Enter Your Email</div><div class="go">GO</div>
</div>
<div class="abs appbanner">
  <div class="phone" role="img" aria-label="Smartphone showing a grocery app"><i></i></div>
  <div class="txt"><div class="o">ORDER</div><div class="g">GROCERIES</div><div class="h">ON YOUR HAND</div></div>
  <div class="dl">DOWNLOAD</div>
</div>
<div class="abs payment">
  <h4>PAYMENT METHODS</h4>
  <div class="cod">CASH <span>ON</span><br><span>DELIVERY</span></div>
  <div class="cards"><i></i><i></i><i></i><i></i><i></i><i></i><i></i><i></i><i></i><i></i></div>
</div>

<!-- welcome -->
<div class="abs welcome">WELCOME TO OUR PAGE</div>
<div class="abs ribbon">
  <svg width="736" height="64" style="position:absolute;left:0;top:0"><path d="M0 16h80v44H0l22-22z" fill="#d2d2d2"/><path d="M736 16h-80v44h80l-22-22z" fill="#d2d2d2"/></svg>
  <div class="band">ONLINE GROCERY SUPERMARKET IN ALL OVER</div>
</div>
<p class="abs intro">Lorem ipsum dolor sit amet diam nonummy nibh euismod nostrud exerci tation hendrerit in vulputate velit soluta nobis eleifend option dynamicus, qui sequitur. Lorem ipsum dolor sit amet diam nonummy nibh euismod nostrud exerci tation hendrerit in vulputate velit &nbsp;soluta nobis eleifend option dynamicus.</p>

<!-- footer -->
<footer class="abs footer">
  <div class="fcol" style="left:107px"><h6>Testimonials</h6>
    <div class="quote">" This is a placeholder version of Lorem Ipsum. Proin gravida nibh vel velit auctor aliquet. Aenean sollicitudin, lorem quis bibendum auctor, nisi elit consequat ipsum "<div class="by">- Clara Whitfield -</div></div>
  </div>
  <div class="fcol" style="left:365px"><h6>My Account</h6><ul><li>My Account</li><li class="on">Login</li><li>My Cart</li><li>Wishlist</li><li>Checkout</li></ul></div>
  <div class="fcol" style="left:537px"><h6>Information</h6><ul><li>About Us</li><li>Delivery Information</li><li>Privacy &amp; Policy</li><li>Terms &amp; Conditions</li><li>Manufactures</li></ul></div>
  <div class="fcol" style="left:710px"><h6>Why Buy From Us</h6><ul><li>Orders &amp; Returns</li><li>Search Terms</li><li>Advance Search</li><li>Affiliates</li><li>Group Sales</li></ul></div>
  <div class="fcol contact" style="left:881px"><h6>Contact Us</h6>
    <p style="margin-top:14px">27 Linden Road, Fernvale, FV3 2PL<br>Telephone: (03) 5550 - 1842<br>E-mail Us: companyname@company.com</p>
    <p style="margin-top:12px;font-style:normal;color:#fff">Follow us :</p>
    <div class="social"><i></i><i></i><i></i><i></i><i></i><i></i><i></i><i></i></div>
  </div>
</footer>
<div class="abs bottombar">2014 © FERNVALEPANTRY.COM.AU &nbsp;&nbsp; All rights reserved</div>

</body>
</html>
```